New business card design needed for Trucking/Staffing company!

I am looking for a business card design. The business name is Keystone Haul Partners, LLC. This company is a staffing company for commercial drivers/truck drivers. Most of our customers are trucking/supply companies. Our colors are blue/black/white/grey. The info I have on my current business cards is
-Spot for a name
-2 lines for an address
-3 lines for Office, cell, and fax
-email
-website(currently on backside of card with logo but can go anywhere)
Updates

Project Deadline Extended
Reason: Open to more designs

Target Market(s)

Trucking companies, building supply companies

Industry/Entity Type

Business

Contact Information for Business Card

Edgy but professional

Font styles to use
Other font styles liked:
• Open to suggestions

Colors
0555a3
000000
ffffff
9d9d9d

Requirements
Must have
• Must have the logo incorporated

```html
<!DOCTYPE html>
<html lang="en">
<head>
<meta charset="utf-8">
<title>Keystone Haul Partners — Business Card</title>
<link rel="stylesheet" href="https://fonts.googleapis.com/css2?family=Open+Sans:wght@400;600&display=swap">
<style>
  :root {
    --backdrop: #3a3431;
    --card: #151515;
    --card-edge: #0a0a0a;
    --brand-blue: #2f3fb8;
    --white: #ffffff;
    --grey: #9d9d9d;
    --text-light: #e6e6e6;
  }
  * { box-sizing: border-box; margin: 0; padding: 0; }
  html, body {
    width: 1200px; height: 844px; overflow: hidden;
    background: var(--backdrop);
    font-family: "Open Sans", Arial, sans-serif;
  }
  .stage {
    position: relative; width: 1200px; height: 844px;
    display: flex; align-items: center; justify-content: center; gap: 60px;
  }
  .card {
    position: relative; width: 520px; height: 298px;
    background: var(--card);
    border: 1px solid var(--card-edge);
    box-shadow: 0 10px 30px rgba(0,0,0,.45);
  }
  .brand {
    position: absolute; display: flex; align-items: center; gap: 10px;
    color: var(--brand-blue); font-weight: 600; letter-spacing: .06em;
    text-transform: uppercase; white-space: nowrap;
  }
  .brand-mark { width: 12px; height: 12px; background: var(--brand-blue); }
  .card-front .brand { left: 34px; top: 58px; font-size: 19px; }
  .card-back .brand { left: 50%; top: 50%; transform: translate(-50%, -50%); font-size: 21px; }

  .contact-list {
    position: absolute; right: 30px; top: 118px;
    list-style: none; text-align: right;
    color: var(--text-light); font-size: 13px; line-height: 20px;
  }
  .contact-list li { display: flex; justify-content: flex-end; align-items: center; gap: 8px; }
  .contact-list svg { width: 11px; height: 11px; fill: var(--grey); flex: none; }
  .contact-list .no-icon { padding-right: 19px; }

  .holder { position: absolute; left: 34px; bottom: 34px; }
  .holder-name { color: var(--grey); font-size: 20px; font-weight: 600; margin-bottom: 6px; }
  .holder-address { color: var(--text-light); font-size: 14px; line-height: 21px; font-style: normal; }
</style>
</head>
<body>
<main class="stage">
  <section class="card card-front">
    <div class="brand"><span class="brand-mark"></span>Keystone Haul Partners</div>

    <ul class="contact-list">
      <li>044-456-7890
        <svg viewBox="0 0 12 12"><path d="M2.5 0.5l2 2.5-1 1.2c.8 1.6 2 2.8 3.6 3.6l1.2-1 2.5 2-1.2 2C5 10.5 1.5 7 0.5 1.7z"/></svg></li>
      <li>123-456-7890
        <svg viewBox="0 0 12 12"><rect x="3" y="0.5" width="6" height="11" rx="1"/></svg></li>
      <li>123-456-7890
        <svg viewBox="0 0 12 12"><rect x="3" y="0.5" width="6" height="3"/><rect x="1" y="4" width="10" height="6" rx="1"/></svg></li>
      <li>123-456-7890
        <svg viewBox="0 0 12 12"><path d="M0.5 2h11v8h-11z M1 2.5l5 4 5-4" stroke="#151515" stroke-width=".8"/></svg></li>
      <li>info@keystonehaul.com
        <svg viewBox="0 0 12 12"><path d="M7.5 1.5a2 2 0 0 1 3 3l-2 2-1-1 2-2a.6.6 0 0 0-1-1l-2 2-1-1zM4.5 10.5a2 2 0 0 1-3-3l2-2 1 1-2 2a.6.6 0 0 0 1 1l2-2 1 1z"/></svg></li>
      <li class="no-icon">www.keystonehaul.com</li>
    </ul>

    <div class="holder">
      <p class="holder-name">Marcus Hale</p>
      <address class="holder-address">12345, Address Goes Here<br>Country Name, 123456</address>
    </div>
  </section>

  <section class="card card-back">
    <div class="brand"><span class="brand-mark"></span>Keystone Haul Partners</div>
  </section>
</main>
</body>
</html>
```